Asia based real estate financing firm needs and AWESOME design for a biz card -Harbor Lending Circle

Looking for a stylish, & corporate-looking business card for a real estate financing brokerage firm in Asia, offering global mortgage loans. I uploaded our current logos. We would like to add a splash of color (perhaps the house icon) or any other suggestions are open. For the winning designer, we have a lot of work! Thanks and best of luck!

Target Market(s)

Real estate investors globally. We want to look more like a BANK and NOT a real estate company. Please don't play up on a "house" design.

Industry/Entity Type

Banking

Contact Information for Business Card

Harbor Lending Circle
Peter Wilks
Co-Founder | Partner

14 Cassia Lane, Suite 310
Singapore 047219
www.hlc-example.asia
peterwilks@hlc-example.asia
+65 555-0142
WeChat: peterwilks

Colors

Designer to choose colors to be used in the design.

Requirements
Must have
• Must have the standard business requirements for a card; name, address, email, etc
• Can be horizontal or vertical.
Nice to have
• It would be great to see some sort of variation to the logo with a pop of color. Red is good as we're in Asia, however, other options work as well.
• Our tag line is - Lending Across Harbors. It doesn't have to be on the card but might be nice.
• I'd like to start seeing our tagline within the cards as well. - Lending Across Harbors.
• Also, please add our location. The location for this card is Singapore so perhaps it can be highlighted or emphasised in some way.
• Singapore | Hong Kong | Shanghai | Manila
• As we will soon open an office in Shanghai, having an option for both languages would be great.
Should not have
• I'm exceited and open to your creativity ... knock it out of the park!

```html
<!DOCTYPE html>
<html lang="en">
<head>
<meta charset="utf-8">
<title>Harbor Lending Circle – Business Card</title>
<link rel="stylesheet" href="https://fonts.googleapis.com/css2?family=Libre+Baskerville:wght@400;700&display=swap">
<style>
  :root {
    --brand-blue: #1660bb;
    --card-slate: #343848;
    --paper: #ffffff;
    --ink-light: #ffffff;
    --ink-soft: #e6e8ee;
    --accent-blue: #1e63c4;
  }
  html, body {
    margin: 0;
    padding: 0;
    width: 902px;
    height: 1200px;
    overflow: hidden;
    background: var(--paper);
    font-family: "Libre Baskerville", Georgia, serif;
  }
  .sheet {
    position: relative;
    width: 902px;
    height: 1200px;
  }
  .card-front {
    position: absolute;
    left: 0; top: 0;
    width: 902px;
    height: 568px;
    background: var(--brand-blue);
  }
  .wordmark {
    position: absolute;
    left: 0; right: 0;
    top: 290px;
    margin: 0;
    text-align: center;
    color: var(--ink-light);
    font-size: 50px;
    font-weight: 400;
    line-height: 1;
  }
  .card-back {
    position: absolute;
    left: 0; top: 634px;
    width: 902px;
    height: 566px;
    background: var(--card-slate);
    color: var(--ink-light);
  }
  .tagline {
    position: absolute;
    left: 62px; top: 71px;
    margin: 0;
    font-size: 22px;
    font-weight: 700;
    letter-spacing: 0.12em;
    text-transform: uppercase;
  }
  .holder-name {
    position: absolute;
    left: 62px; top: 218px;
    margin: 0;
    font-size: 35px;
    font-weight: 700;
    letter-spacing: 0.02em;
  }
  .holder-title {
    position: absolute;
    left: 62px; top: 272px;
    margin: 0;
    font-size: 16px;
    color: var(--ink-soft);
  }
  .contact-block {
    position: absolute;
    top: 398px;
    font-size: 16px;
    line-height: 26px;
    color: var(--ink-soft);
  }
  .contact-label {
    display: block;
    margin-bottom: 16px;
    font-size: 16px;
    font-weight: 700;
    color: var(--ink-light);
  }
  .contact-address { left: 62px; }
  .contact-phone { left: 295px; }
  .contact-web { left: 662px; top: 436px; font-size: 15px; white-space: nowrap; }
  .contact-block strong { font-weight: 700; color: var(--ink-light); }
  .web-icon {
    position: absolute;
    left: 676px; top: 380px;
    width: 32px; height: 32px;
  }
</style>
</head>
<body>
<div class="sheet">
  <section class="card-front">
    <h1 class="wordmark">Harbor Lending Circle</h1>
  </section>

  <section class="card-back">
    <p class="tagline">Lending Across Harbors</p>
    <h2 class="holder-name">Peter Wilks</h2>
    <p class="holder-title">Co-Founder | Partner</p>

    <div class="contact-block contact-address">
      <span class="contact-label">Address</span>
      14 Cassia Lane,<br>
      Suite 310 <strong>Singapore</strong>
    </div>

    <div class="contact-block contact-phone">
      <span class="contact-label">Phone</span>
      +65 555-0142<br>
      WeChat: peterwilks
    </div>

    <svg class="web-icon" viewBox="0 0 32 32" aria-hidden="true">
      <circle cx="16" cy="16" r="14" fill="none" stroke="var(--accent-blue)" stroke-width="2.5"/>
      <circle cx="16" cy="16" r="7" fill="none" stroke="var(--accent-blue)" stroke-width="1.6"/>
      <line x1="9" y1="16" x2="23" y2="16" stroke="var(--accent-blue)" stroke-width="1.4"/>
      <ellipse cx="16" cy="16" rx="3" ry="7" fill="none" stroke="var(--accent-blue)" stroke-width="1.4"/>
    </svg>

    <div class="contact-block contact-web">
      www.hlc-example.asia<br>
      peterwilks@hlc-example.asia
    </div>
  </section>
</div>
</body>
</html>
```